Business Card Design

Consultation for design, construction athletic facilities specializing in synthetic turf systems and all weather running track systems.
Motto "True Owner Representation"
New Company that we'd like to highlight the LOGO first and foremost with the colors of the background and font as primary colors of the card too if possible. I've also attached a typical larger project design layout that could be used in the background to highlight our design and construction specialty.
Website is something we want very noticeable for driving traffic.
Target Market(s)
Athletic Directors, Designers, Government and Military, Contractors
Industry/Entity Type
Construction
Contact Information for Business Card
Peter L. Vandrell CFB, CTB
48317 W 63rd Ave
Harlow Ridge, WA 99482
C +1 503.555.0147
O +1 808.555.0182
Peter@fieldlaneco.example
www.fieldlaneco.example

```html
<!DOCTYPE html>
<html lang="en">
<head>
<meta charset="utf-8">
<title>Caldera Sport — Business Card</title>
<link rel="stylesheet" href="https://fonts.googleapis.com/css2?family=EB+Garamond:wght@400;600&display=swap">
<style>
  :root {
    --page: #d9d6d1;
    --card-black: #060606;
    --card-black-soft: #1a1a1a;
    --band-grey: #3c3c3e;
    --band-grey-light: #5a5a5c;
    --gold: #e2a83a;
    --gold-deep: #b97a1c;
    --logo-copper: #d98a4a;
    --text-light: #cfcfcf;
    --plan-grey: #cfcfcf;
  }
  * { box-sizing: border-box; margin: 0; padding: 0; }
  html, body {
    width: 1200px; height: 900px; overflow: hidden;
    background: var(--page);
    font-family: "EB Garamond", Georgia, serif;
  }
  .sheet {
    width: 1200px; height: 900px;
    display: flex; flex-direction: column; align-items: center; justify-content: center;
    gap: 48px;
  }
  .card {
    position: relative;
    width: 570px; height: 326px;
    border-radius: 4px;
    overflow: hidden;
    box-shadow: 0 14px 30px rgba(0,0,0,.35);
  }

  /* Front */
  .card-front { background: var(--card-black); }
  .flare-area {
    position: absolute; right: 0; top: 0;
    width: 62%; height: 70%;
    background: radial-gradient(ellipse at 65% 25%, rgba(255,214,140,.85) 0%, rgba(226,168,58,.55) 14%, rgba(185,122,28,.2) 38%, rgba(6,6,6,0) 68%);
  }
  .site-plan {
    position: absolute; left: 44px; top: 78px;
    width: 172px; height: 172px; border-radius: 50%;
    background: radial-gradient(circle at 45% 45%, #f2f2f2 0%, var(--plan-grey) 100%);
  }
  .front-website {
    position: absolute; left: 40px; bottom: 26px;
    color: var(--gold); font-size: 17px; letter-spacing: .3px;
  }

  /* Back */
  .card-back {
    background: linear-gradient(160deg, var(--card-black-soft) 0%, var(--card-black) 55%);
  }
  .info-band {
    position: absolute; left: 0; right: 0; bottom: 0; height: 44%;
    background: linear-gradient(180deg, var(--band-grey-light) 0%, var(--band-grey) 100%);
    border-top: 1px solid #777;
  }
  .brand {
    position: absolute; left: 0; right: 0; top: 58px;
    display: flex; align-items: center; justify-content: center; gap: 14px;
  }
  .brand-dot { width: 16px; height: 16px; border-radius: 50%; background: var(--logo-copper); }
  .brand-name {
    color: var(--logo-copper); font-size: 34px; font-weight: 400; letter-spacing: 3px;
  }
  .contact {
    position: absolute; left: 0; right: 0; top: 150px;
    text-align: center; color: var(--text-light); font-size: 15px; line-height: 1.55;
  }
  .contact-name {
    color: var(--gold); font-weight: 600; font-size: 19px; margin-bottom: 6px;
  }
</style>
</head>
<body>
<main class="sheet">
  <section class="card card-front">
    <div class="flare-area" role="img" aria-label="Golden light flare artwork on black"></div>
    <div class="site-plan" role="img" aria-label="Athletic facility site plan with running track and fields"></div>
    <p class="front-website">www.fieldlaneco.example</p>
  </section>

  <section class="card card-back">
    <div class="info-band"></div>
    <div class="brand">
      <span class="brand-dot"></span>
      <span class="brand-name">Caldera Sport</span>
    </div>
    <div class="contact">
      <p class="contact-name">Peter L. Vandrell</p>
      <p>CFB, CTB 48317 W 63rd Ave Harlow Ridge, WA 99482</p>
      <p>C +1 503.555.0147 O +1 808.555.0182</p>
      <p>E: Peter@fieldlaneco.example</p>
    </div>
  </section>
</main>
</body>
</html>
```